依頼詳細
レスポンシブウェブデザインを意識したデザインでお願いします。
参考URL
https://morisato-koubou.jp/

デザインに関しては、添付してあるデザインレイアウトシートを基にお願いします。

まずはパソコンサイトのデザインをお願いします。
当選後、スマホデザインをお願いします。

既存のテンプレートを使う場合は
テンプレート名を下記のような記載を提案の中にいれてください。
例:WordpressテーマはKandoria、デザインスキンは無料のHLM2019 RX4(http://kandoria.com/ex_plugin/hlmnagoya2019_rx4/)をベースにデザインいたしました。
など

素材となる写真は現在、撮影中ですので、一旦他のサイトや参考URLの写真をサンプルとして入れてください。(サンプルなどの表記をお願いします)
また、購入が必要な写真などを利用した場合は、Pelmora Stock(https://stock.pelmora.com/jp/)からファイル番号と価格を教えてください。
ページ数
1ページ
希望イメージ
シンプル 複雑
単色 カラフル
暗い 明るい
日常 高級
遊び心 厳粛
未来的 伝統的
女性的 男性的
希望する色
茶系、緑系
納品ファイル
• イラストレーター形式 (.ai)
• フォトショップ形式 (.psd)
• PNG形式 (.png)
補足説明
上記のいずれか1つ。アウトラインありとなしの2つ。

クライアントのイメージ通りでした。

たくさんのご提案ありがとうございました。
次回もぜひ、よろしくお願い致します。

```html
<!DOCTYPE html>
<html lang="ja">
<head>
<meta charset="utf-8">
<title>株式会社キノハ</title>
<link rel="stylesheet" href="https://fonts.googleapis.com/css2?family=Noto+Sans+JP:wght@400;500;700&family=Noto+Serif+JP:wght@500;700&display=swap">
<style>
:root{
  --ink:#333330;
  --muted:#77756f;
  --line:#d6d3cc;
  --paper:#ffffff;
  --stone:#f1efeb;
  --sand:#dcd4c3;
  --olive:#7c7658;
  --forest:#4d5a43;
  --wood:#d6b88a;
  --wood-dark:#9c7a4c;
  --mint:#a9d3c6;
  --rose:#c7a29b;
  --sage:#9a9b7b;
  --cream:#e9dcc6;
}
*{box-sizing:border-box;margin:0;padding:0}
html,body{width:1200px;height:4380px;overflow:hidden}
body{font-family:"Noto Sans JP",sans-serif;color:var(--ink);background:var(--paper);font-size:14px;line-height:1.7;position:relative}
.section-title{font-family:"Noto Serif JP",serif;font-weight:700;font-size:28px;text-align:center;letter-spacing:.08em}
.section-lead{font-size:12px;text-align:center;color:var(--muted);margin-top:6px;letter-spacing:.05em}

/* header */
.site-header{height:150px;text-align:center;padding-top:18px}
.brand{display:inline-flex;align-items:center;gap:10px;font-family:"Noto Sans JP",sans-serif;font-weight:700;font-size:24px;letter-spacing:.08em}
.brand-mark{width:26px;height:26px;background:var(--ink)}
.global-nav{display:flex;justify-content:center;gap:0;margin-top:62px}
.global-nav a{color:var(--ink);text-decoration:none;font-size:13px;padding:0 34px;border-left:1px solid var(--line)}
.global-nav a:last-child{border-right:1px solid var(--line)}
.side-contact{position:absolute;left:0;top:180px;width:44px;height:200px;background:var(--forest);color:#fff;writing-mode:vertical-rl;font-size:13px;display:flex;align-items:center;justify-content:center;letter-spacing:.2em;z-index:2}

.hero{height:400px;background:linear-gradient(100deg,#e5cfa8 0%,#f4f1ec 30%,#f6f4f0 55%,#efe3cf 80%,#e2c79d 100%)}

/* strengths */
.strengths{height:420px;padding-top:30px}
.strength-list{display:flex;gap:14px;justify-content:center;margin-top:72px}
.strength-card{width:176px;text-align:center}
.strength-photo{height:124px;position:relative}
.more-tag{position:absolute;right:0;top:0;background:var(--ink);color:#fff;font-size:10px;padding:1px 8px}
.strength-card p{font-size:12px;margin-top:10px;line-height:1.5}

/* business */
.business{padding-top:10px}
.business-grid{display:grid;grid-template-columns:1fr 1fr;margin-top:60px}
.business-tile{height:220px;position:relative}
.business-tile .copy{position:absolute;right:20px;top:70px;width:300px;background:rgba(255,255,255,.88);font-size:11px;padding:10px 12px;line-height:1.6}
.business-tile .label{position:absolute;left:0;bottom:24px;background:rgba(255,255,255,.9);font-weight:700;font-size:16px;padding:4px 30px 4px 36px}

/* works */
.works{height:520px;padding-top:50px}
.card-row{display:flex;justify-content:center;gap:18px;margin-top:64px}
.case-card{width:196px}
.case-photo{height:150px}
.case-card p{font-size:12px;margin-top:12px;padding:0 6px;line-height:1.6}

/* news */
.news{width:960px;margin:60px auto 0;height:320px}
.news-head{display:flex;justify-content:space-between;align-items:flex-end;border-bottom:2px solid var(--ink);padding-bottom:8px}
.news-head h2{font-size:20px;font-weight:700;border-left:4px solid var(--ink);padding-left:12px;line-height:1.2}
.news-head a{font-size:12px;color:var(--ink);text-decoration:none}
.news-list{list-style:none}
.news-list li{display:flex;gap:40px;border-bottom:1px solid var(--line);padding:10px 8px;font-size:12px}
.news-list time{width:70px;color:var(--muted)}

/* blog */
.blog{height:540px;padding-top:90px}
.blog .card-row{margin-top:60px}
.blog time{display:block;text-align:center;font-size:12px;margin-bottom:6px}
.blog .case-photo{height:140px}

/* faq */
.faq{height:560px;padding-top:10px}
.faq-mark{text-align:center;font-family:"Noto Serif JP",serif;font-weight:700;font-size:58px;line-height:1}
.faq .section-lead{font-size:16px;color:var(--ink);margin-top:10px}
.faq-list{width:960px;margin:40px auto 0}
.faq-item{border-bottom:1px solid var(--line);padding:14px 0 16px}
.faq-q,.faq-a{display:flex;gap:18px;align-items:baseline}
.faq-q{font-weight:700;font-size:15px}
.faq-a{font-size:12px;color:var(--muted);margin-top:8px}
.faq-q span,.faq-a span{font-family:"Noto Serif JP",serif;font-size:22px;color:var(--ink);width:20px}

/* contact */
.contact{position:absolute;left:0;top:3510px;width:1200px;height:560px;background:var(--sand);padding-top:40px}
.contact-lead{font-size:12px;text-align:center;margin-top:28px;line-height:1.8}
.contact-form{width:760px;margin:40px auto 0}
.form-row{display:flex;align-items:flex-start;margin-bottom:14px}
.form-row label{width:150px;font-size:13px;padding-top:4px}
.form-row .field{flex:1;height:30px;background:#fff;border:1px solid #c9c1b0}
.form-row .field.tall{height:120px}
.form-actions{display:flex;justify-content:center;gap:14px;margin-top:26px}
.btn{font-size:12px;padding:8px 26px;border:1px solid var(--olive);background:#fff;color:var(--ink)}
.btn.primary{background:var(--olive);color:#fff}

/* footer */
.site-footer{position:absolute;left:0;top:4070px;width:1200px;height:310px;border-top:1px solid var(--line);padding:40px 60px 0}
.footer-top{display:flex;align-items:center;justify-content:space-between}
.footer-tel{display:flex;align-items:center;gap:10px;font-size:30px;font-weight:500;margin-left:auto;margin-right:30px}
.footer-btn{background:var(--olive);color:#fff;font-size:14px;padding:10px 30px}
.footer-bottom{display:flex;justify-content:space-between;margin-top:34px;font-size:12px}
.footer-nav{display:flex;gap:26px}
.copyright{text-align:center;font-size:11px;color:var(--muted);margin-top:80px}
</style>
</head>
<body>

<header class="site-header">
  <div class="brand"><span class="brand-mark"></span>株式会社キノハ</div>
  <nav class="global-nav">
    <a href="#">弊社の強み</a><a href="#">事業案内</a><a href="#">加工事例・商品紹介</a><a href="#">会社案内</a><a href="#">よくある質問</a>
  </nav>
</header>
<a class="side-contact">お問い合わせ</a>

<div class="hero" role="img" aria-label="木製トレー、木製スタンド、積み木、木の器、年輪の丸太断面を並べたメイン写真"></div>

<section class="strengths">
  <h2 class="section-title">弊社の強み</h2>
  <p class="section-lead">木製品の加工・組立・梱包・木材一般販売</p>
  <div class="strength-list">
    <div class="strength-card"><div class="strength-photo" role="img" aria-label="住宅部材の木材写真" style="background:#d7b889"><span class="more-tag">詳しく</span></div><p>住宅部材 加工・組立</p></div>
    <div class="strength-card"><div class="strength-photo" role="img" aria-label="産業機器用木枠の写真" style="background:#c9b79b"><span class="more-tag">詳しく</span></div><p>産業機器（コンベアー）<br>加工・組立</p></div>
    <div class="strength-card"><div class="strength-photo" role="img" aria-label="治具用合板の写真" style="background:#dcc29a"><span class="more-tag">詳しく</span></div><p>治具類・ハネ入加工</p></div>
    <div class="strength-card"><div class="strength-photo" role="img" aria-label="梱包資材の倉庫写真" style="background:#a39a8c"><span class="more-tag">詳しく</span></div><p>梱包資材・梱包請負</p></div>
    <div class="strength-card"><div class="strength-photo" role="img" aria-label="木製パレットの写真" style="background:#b99b70"><span class="more-tag">詳しく</span></div><p>その他 加工品</p></div>
  </div>
</section>

<section class="business">
  <h2 class="section-title">事業案内</h2>
  <p class="section-lead">木製品の加工・組立・梱包・木材一般販売</p>
  <div class="business-grid">
    <div class="business-tile" role="img" aria-label="丸太の年輪の写真" style="background:linear-gradient(90deg,#d8b888,#e8d3ae)"><p class="copy">木製品の加工と組立、梱包まで一貫して対応します。材料の調達から納品まで、安心してご依頼ください。</p><span class="label">材料</span></div>
    <div class="business-tile" role="img" aria-label="工具の写真" style="background:linear-gradient(90deg,#d9d9d6,#bcbcb8)"><p class="copy">木製品の加工と組立、梱包まで一貫して対応します。材料の調達から納品まで、安心してご依頼ください。</p><span class="label">加工・組立</span></div>
    <div class="business-tile" role="img" aria-label="加工機械の写真" style="background:linear-gradient(90deg,#8d8a80,#b9b4a6)"><p class="copy">木製品の加工と組立、梱包まで一貫して対応します。材料の調達から納品まで、安心してご依頼ください。</p><span class="label">設備</span></div>
    <div class="business-tile" role="img" aria-label="木材の寸法を測る手元の写真" style="background:linear-gradient(90deg,#c9a274,#e3cba4)"><p class="copy">木製品の加工と組立、梱包まで一貫して対応します。材料の調達から納品まで、安心してご依頼ください。</p><span class="label">オーダーメイド</span></div>
  </div>
</section>

<section class="works">
  <h2 class="section-title">加工事例</h2>
  <p class="section-lead">ご依頼いただきました事例を一部ご紹介いたします</p>
  <div class="card-row">
    <div class="case-card"><div class="case-photo" role="img" aria-label="木製スタンドの写真" style="background:var(--mint)"></div><p>木製品の加工と組立を、確かな技術と丁寧な仕上げで行いました。</p></div>
    <div class="case-card"><div class="case-photo" role="img" aria-label="木製の仕切り箱の写真" style="background:#7a5c43"></div><p>木製品の加工と組立を、確かな技術と丁寧な仕上げで行いました。</p></div>
    <div class="case-card"><div class="case-photo" role="img" aria-label="木製スタンドの写真" style="background:var(--rose)"></div><p>木製品の加工と組立を、確かな技術と丁寧な仕上げで行いました。</p></div>
    <div class="case-card"><div class="case-photo" role="img" aria-label="木の積み木の写真" style="background:var(--cream)"></div><p>木製品の加工と組立を、確かな技術と丁寧な仕上げで行いました。</p></div>
    <div class="case-card"><div class="case-photo" role="img" aria-label="木製スタンドの写真" style="background:var(--sage)"></div><p>木製品の加工と組立を、確かな技術と丁寧な仕上げで行いました。</p></div>
  </div>
</section>

<section class="news">
  <div class="news-head"><h2>お知らせ</h2><a href="#">一覧 ›</a></div>
  <ul class="news-list">
    <li><time>19.10.22</time><span>年末年始の営業日についてのお知らせを掲載しました。ご確認ください。</span></li>
    <li><time>19.8.10</time><span>夏季休業期間中のお問い合わせについてのご案内です。</span></li>
    <li><time>19.8.2</time><span>新しい加工設備を導入いたしました。詳しくはブログをご覧ください。</span></li>
    <li><time>19.5.7</time><span>大型連休明けの出荷スケジュールについてお知らせします。</span></li>
    <li><time>19.0.1</time><span>ホームページを開設しました。</span></li>
  </ul>
</section>

<section class="blog">
  <h2 class="section-title">ブログ</h2>
  <p class="section-lead">日々の弊社の取り組み・新着品など</p>
  <div class="card-row">
    <div class="case-card"><time>19.6.1</time><div class="case-photo" role="img" aria-label="木製スタンドの写真" style="background:var(--mint)"></div><p>木製品の加工と組立を、確かな技術と丁寧な仕上げで行いました。</p></div>
    <div class="case-card"><time>19.6.1</time><div class="case-photo" role="img" aria-label="木製の仕切り箱の写真" style="background:#7a5c43"></div><p>木製品の加工と組立を、確かな技術と丁寧な仕上げで行いました。</p></div>
    <div class="case-card"><time>19.6.1</time><div class="case-photo" role="img" aria-label="木製スタンドの写真" style="background:var(--rose)"></div><p>木製品の加工と組立を、確かな技術と丁寧な仕上げで行いました。</p></div>
    <div class="case-card"><time>19.6.1</time><div class="case-photo" role="img" aria-label="木の積み木の写真" style="background:var(--cream)"></div><p>木製品の加工と組立を、確かな技術と丁寧な仕上げで行いました。</p></div>
    <div class="case-card"><time>19.6.1</time><div class="case-photo" role="img" aria-label="木製スタンドの写真" style="background:var(--sage)"></div><p>木製品の加工と組立を、確かな技術と丁寧な仕上げで行いました。</p></div>
  </div>
</section>

<section class="faq">
  <div class="faq-mark">Q&amp;A</div>
  <p class="section-lead">よくあるご質問</p>
  <div class="faq-list">
    <div class="faq-item"><p class="faq-q"><span>Q</span>見積りは無料ですか？</p><p class="faq-a"><span>A</span>はい、無料でございます。お気軽にご相談ください。</p></div>
    <div class="faq-item"><p class="faq-q"><span>Q</span>利用内容の変更で、何度も見積依頼しても大丈夫ですか？</p><p class="faq-a"><span>A</span>はい、何度でも承ります。ご利用内容に合わせて最適なお見積りをご提示いたします。</p></div>
    <div class="faq-item"><p class="faq-q"><span>Q</span>キャンセル料を発生しますか？</p><p class="faq-a"><span>A</span>はい。ご依頼後のキャンセルは下記の通りとなります。<br>作業開始前：無料　／　作業途中：50%　／　作業完了後：100%</p></div>
    <div class="faq-item"><p class="faq-q"><span>Q</span>クレジットカードで料金をお支払いすることはできますか？</p><p class="faq-a"><span>A</span>お支払いは銀行振込を基本としております。詳しくは担当者までお問い合わせください。</p></div>
  </div>
</section>

<section class="contact">
  <h2 class="section-title">お問い合わせ</h2>
  <p class="contact-lead">下記フォームに必要事項を入力の上送信してください。<br>弊社より、内容を確認後折り返しご連絡させていただきます。</p>
  <div class="contact-form">
    <div class="form-row"><label>お名前</label><div class="field"></div></div>
    <div class="form-row"><label>電話番号</label><div class="field"></div></div>
    <div class="form-row"><label>メールアドレス</label><div class="field"></div></div>
    <div class="form-row"><label>お問い合わせ<br>内容</label><div class="field tall"></div></div>
    <div class="form-actions"><span class="btn">リセット</span><span class="btn primary">送信内容の確認画面へ</span></div>
  </div>
</section>

<footer class="site-footer">
  <div class="footer-top">
    <div class="brand"><span class="brand-mark"></span>株式会社キノハ</div>
    <div class="footer-tel">
      <svg width="26" height="26" viewBox="0 0 24 24" aria-hidden="true"><path fill="#333330" d="M6.6 10.8a15.2 15.2 0 0 0 6.6 6.6l2.2-2.2c.3-.3.7-.4 1-.2 1.1.4 2.3.6 3.6.6.6 0 1 .4 1 1V20c0 .6-.4 1-1 1A17 17 0 0 1 3 4c0-.6.4-1 1-1h3.5c.6 0 1 .4 1 1 0 1.3.2 2.5.6 3.6.1.3 0 .7-.2 1z"/></svg>
      0276-55-0192
    </div>
    <span class="footer-btn">お問い合わせ</span>
  </div>
  <div class="footer-bottom">
    <p>〒370-0000 緑川県森里市中央町3000-1</p>
    <nav class="footer-nav"><span>弊社の強み</span><span>事業案内</span><span>加工事例・商品紹介</span><span>会社案内</span><span>よくある質問</span></nav>
  </div>
  <p class="copyright">Copyright © 株式会社キノハ All Rights Reserved.</p>
</footer>

</body>
</html>
```